VFX Company Business Card Design Project

The Pixel Harbor is a decentralized Visual Effects Studio servicing the television and feature film industries.
Project Brief:
Take our logo that was previously designed on Sketch Forum and make a double sided business card.
Requirements:
- Card MUST be double sided.
- Front of card MUST have the yellow part of our logo against the dark grey background.
- Back of card is completely up to the designer.
- Back of card must include the complete company logo.
Please follow these File Preparation guidelines:
http://printmarlow.example/infopage?file=filetype_en&s=PrintMarlow_new&lang=en
Industry/Entity Type
Business
Look and feel
Each slider illustrates characteristics of the customer's brand and the style your logo design should communicate.

```html
<!DOCTYPE html>
<html lang="en">
<head>
<meta charset="utf-8">
<title>The Pixel Harbor – Business Card</title>
<link href="https://fonts.googleapis.com/css2?family=Montserrat:wght@400;600;800&family=Open+Sans:wght@400;600;700&display=swap" rel="stylesheet">
<style>
  :root {
    --backdrop: #b9b9b7;
    --card-dark: #262728;
    --band: #75838a;
    --brand-yellow: #f8c51f;
    --text-light: #eef1f2;
    --text-muted: #dfe4e6;
    --white: #ffffff;
  }
  * { margin: 0; padding: 0; box-sizing: border-box; }
  html, body { width: 1200px; height: 1023px; overflow: hidden; }
  body {
    background: var(--backdrop);
    position: relative;
    font-family: "Open Sans", Arial, sans-serif;
  }
  .card {
    position: absolute;
    width: 580px;
    height: 331px;
    border-radius: 16px;
    overflow: hidden;
    box-shadow: 0 10px 24px rgba(0,0,0,0.25);
  }
  /* Front side */
  .card-front { left: 70px; top: 120px; background: var(--card-dark); }
  .card-front .wordmark {
    position: absolute; left: 40px; top: 58px;
    font-family: "Montserrat", Arial, sans-serif;
    font-weight: 800; font-size: 40px; letter-spacing: 0.5px;
    color: var(--brand-yellow);
    display: flex; align-items: center; gap: 14px;
  }
  .wordmark .mark-dot {
    width: 26px; height: 26px; border-radius: 50%;
    background: currentColor; flex: none;
  }
  .info-band {
    position: absolute; left: 0; right: 0; bottom: 0; height: 150px;
    background: var(--band);
  }
  .accent-circle {
    position: absolute; right: 36px; bottom: 96px;
    width: 96px; height: 96px; border-radius: 50%;
    background: var(--brand-yellow);
  }
  .person { position: absolute; left: 40px; top: 28px; color: var(--text-light); }
  .person-name { font-weight: 700; font-size: 17px; letter-spacing: 0.5px; text-transform: uppercase; }
  .person-title { font-size: 13px; margin-top: 2px; }
  .address {
    position: absolute; left: 40px; bottom: 22px;
    font-size: 12.5px; line-height: 1.5; color: var(--text-muted);
  }
  .contacts {
    position: absolute; left: 300px; top: 24px; list-style: none;
    font-size: 12.5px; line-height: 1; color: var(--text-light);
  }
  .contacts li { display: flex; align-items: center; gap: 8px; margin-bottom: 9px; }
  .contacts svg { width: 13px; height: 13px; flex: none; }
  /* Back side */
  .card-back { left: 550px; top: 560px; background: var(--brand-yellow); }
  .card-back .wordmark {
    position: absolute; left: 0; right: 0; top: 120px; text-align: center;
    font-family: "Montserrat", Arial, sans-serif;
    font-weight: 800; font-size: 44px; color: var(--white);
  }
  .card-back .site {
    position: absolute; left: 0; right: 0; bottom: 40px; text-align: center;
    font-family: "Montserrat", Arial, sans-serif;
    font-weight: 600; font-size: 14px; letter-spacing: 5px; color: var(--white);
  }
</style>
</head>
<body>

<section class="card card-front" aria-label="Business card front">
  <div class="wordmark"><span class="mark-dot"></span>The Pixel Harbor</div>
  <div class="accent-circle"></div>
  <div class="info-band">
    <div class="person">
      <p class="person-name">Dana Reyes</p>
      <p class="person-title">President</p>
    </div>
    <p class="address">27 Quayside Lane<br>Harborview OR 97000<br>www.pixelharbor.example</p>
    <ul class="contacts">
      <li>
        <svg viewBox="0 0 14 14"><rect x="3" y="1" width="8" height="12" rx="1.5" fill="var(--brand-yellow)"/><rect x="5" y="3" width="4" height="6" fill="var(--band)"/></svg>
        +1 555.210.0187
      </li>
      <li>
        <svg viewBox="0 0 14 14"><circle cx="7" cy="7" r="6.5" fill="var(--brand-yellow)"/><path d="M4.5 3.8c.6-.4 1.2 0 1.4.6l.3 1c.1.4-.2.7-.5.9.4.9 1 1.5 1.9 1.9.2-.3.5-.6.9-.5l1 .3c.6.2 1 .8.6 1.4-.5.7-1.5.9-2.4.4C6 9 5 8 4.2 6.3c-.5-.9-.3-1.9.3-2.5z" fill="var(--band)"/></svg>
        +1 555.210.0344
      </li>
      <li>
        <svg viewBox="0 0 14 14"><rect x="1" y="4" width="12" height="8" rx="1" fill="var(--brand-yellow)"/><rect x="3.5" y="1" width="7" height="4" fill="var(--brand-yellow)"/><rect x="3.5" y="7" width="7" height="3" fill="var(--band)"/></svg>
        +1 555.480.0344
      </li>
      <li>
        <svg viewBox="0 0 14 14"><rect x="1" y="3" width="12" height="8" rx="1" fill="var(--brand-yellow)"/><path d="M1.5 3.5 7 8l5.5-4.5" fill="none" stroke="var(--band)" stroke-width="1.2"/></svg>
        hello@pixelharbor.example
      </li>
    </ul>
  </div>
</section>

<section class="card card-back" aria-label="Business card back">
  <div class="wordmark">The Pixel Harbor</div>
  <p class="site">www.pixelharbor.example</p>
</section>

</body>
</html>
```